Wine labels Velmora Wine Council - Nueva etiqueta El Consejo Regulador de vinos de Albarrán

Velmora Wines Council, based in southern Spain, are looking to create a new suite of wine labels which retain the elegance of the Sherry Wines industry while reinvigorating their image to the modern era and a new generation of Sherry Wine lovers. These labels will be used across the Velmora Wines Council's range of wines for the promotion of the Sherry Wines industry.

Your design must present at least two styles of Sherry Wines which demonstrate an elegant, modern interpretation and understanding of the unique mood and personality for these wines and the essence of southern Spain.

10 labels will be created based on the winning design, one for each of the unique varieties of Sherry Wines within the collection. This collection comprises of several different wine varieties including: Fino, Manzanilla, Amontillado, Oloroso, Palo Cortado, Medium, Cream, Pale Cream, Pedro Ximenez and Moscatel.

We recommend you visit our website www.velmora-vinos.example/wines as the source to understanding the origins and unique personality of these diverse wines.

El Consejo Regulador de los Vinos de Albarrán y Tordesal quiere renovar las etiquetas de los vinos utilizados para sus actividades de promoción genérica. Esta colección de vinos comprende las tipologías más importantes de la región que incluye: fino, manzanilla, amontillado, oloroso, palo cortado, pale cream, medium, cream, pedro ximénez y moscatel. Por lo tanto se precisan 10 etiquetas, una para cada uno de los vinos mencionados.
Updates

Project Deadline Extended
Reason: Due to some confusion with the deadline we wish to officially extend the deadline to allow designers one last week to submit their entries.

Target Market(s)

Industry, journalists, media, sommeliers, chefs, wine writers

Industry/Entity Type

Council

Requirements
Must have
• Front and Back label plus capsule:
• Front label can have either of the two official logos of the Velmora Wine council titled Vinos de Albarrán Digital or not, this is optional. Must include: Vino selecionado por el Consejo Regulador de la Denominacion de Origen, Name of the variety of wine eg FINO, percentage of alcohol eg 15% and quantity 75 cl.
• The back of the label must include the council logo titled Sellora and 4 additional logos positioned smaller. The Europa logo must appear larger than the 3 other logos. Space for descriptive text about the wine is also required.
• The dimensions of the bottle can be found at this link http://www.vidrialto.example/es/catalogo/vinos-y-espumosos/bordelesas/bd-orla
• Altura:305 mm
• Diámetro base:76,20 mm
• Diámetro hombro:82 mm
• Tipo boca:Cetie
• Peso:750 gr
• Capacidad:75 cl
• Etiqueta delantera y trasera y capsula
• La etiqueta delantera puede incluir el logo oficial del Consejo Regulador o el logo digital, o ninguno, esto es opcional. Debe incluir el siguiete texto: Vino selecionado por el Consejo Regulador de la Denominacion de Origen, el nombre de la variedad del vino, por ejemplo Fino, el porcentaje de alcohol, por ejemplo 15%, y la capacidad 75cl.
• La etiqueta trasera debe incluir el logo oficial Sellora del Consejo, y cuatro logos adicionales con una dimension menor. El Logo de ¨Campos Vivos Rurales¨ debe ser de mayor tamaño que los otros. Se precisa espacio para el texto descriptivo de los vinos.
• Las dimensiones de la botella se puede encontrar en este enlace
• http://www.vidrialto.example/es/catalogo/vinos-y-espumosos/bordelesas/bd-orla
• Altura:305 mm
• Diámetro base:76,20 mm
• Diámetro hombro:82 mm
• Tipo boca:Cetie
• Peso:750 gr
• Capacidad:75 cl
Nice to have
• See our website velmora-vinos.example to understand the origin of the wines. Ver nuestra página web velmora-vinos.example para mejor entender los vinos.
Should not have
• Images of catavinos or stereotypical images from Spain such as flamenco dancers or guitars.

```html
<!DOCTYPE html>
<html lang="es">
<head>
<meta charset="utf-8">
<title>Manzanilla – etiqueta delantera, trasera y cápsula</title>
<link rel="stylesheet" href="https://fonts.googleapis.com/css2?family=Playball&family=Alegreya+Sans:wght@300;400&family=Bodoni+Moda:wght@500&display=swap">
<style>
  :root {
    --paper: #ffffff;
    --label-black: #0a0305;
    --ink-light: #d8d4ce;
    --ink-soft: #bdb9b3;
    --gold: #f2dc82;
    --gold-line: #6b5a22;
    --photo-dark: #1b1816;
    --photo-mid: #7d776f;
    --photo-light: #cfcbc2;
  }
  * { margin: 0; padding: 0; box-sizing: border-box; }
  html, body { width: 1200px; height: 1000px; overflow: hidden; background: var(--paper); }
  .canvas { position: relative; width: 1200px; height: 1000px; }

  .front-label {
    position: absolute; left: 38px; top: 37px; width: 655px; height: 924px;
    background: var(--label-black);
  }
  .front-photo {
    position: absolute; left: 92px; top: 62px; width: 480px; height: 505px;
    background: radial-gradient(ellipse closest-side at 55% 58%, var(--photo-light) 0%, var(--photo-mid) 45%, var(--photo-dark) 80%, transparent 100%);
  }
  .variety {
    font-family: "Playball", cursive; color: var(--ink-light); font-weight: 400;
    text-align: center; white-space: nowrap;
  }
  .front-label .variety {
    position: absolute; left: 0; right: 0; top: 628px; font-size: 74px; line-height: 1;
  }
  .front-label .council-note {
    position: absolute; left: 0; right: 0; top: 728px; text-align: center;
    font-family: "Alegreya Sans", sans-serif; font-weight: 300; font-size: 12.5px;
    line-height: 18px; color: var(--ink-light);
  }
  .measure {
    position: absolute; top: 870px; display: inline-block; font-family: "Bodoni Moda", serif; font-weight: 500;
    font-size: 20px; color: var(--ink-light); transform: scaleX(0.72);
  }
  .measure.volume { left: 20px; transform-origin: left center; }
  .measure.alcohol { right: 20px; transform-origin: right center; }

  .back-label {
    position: absolute; left: 773px; top: 37px; width: 385px; height: 604px;
    background: var(--label-black);
  }
  .back-label .variety {
    position: absolute; left: 0; right: 0; top: 64px; font-size: 36px; line-height: 1;
  }
  .back-label .tagline {
    position: absolute; left: 0; right: 0; top: 110px; text-align: center;
    font-family: "Alegreya Sans", sans-serif; font-weight: 300; font-size: 11px; color: var(--ink-light);
  }
  .origin-seal {
    position: absolute; left: 153px; top: 373px; width: 80px; height: 103px;
    background: #f4f1e8; border: 2px solid #c9a94a; border-radius: 6px;
  }
  .partner-row {
    position: absolute; left: 15px; right: 15px; top: 540px; height: 55px;
    display: flex; align-items: center; justify-content: space-between; color: var(--ink-light);
    font-family: "Alegreya Sans", sans-serif; font-weight: 400;
  }
  .partner.main { font-size: 15px; line-height: 17px; width: 140px; }
  .partner { font-size: 9px; line-height: 11px; text-align: center; }
  .partner .mark-circle {
    display: block; width: 36px; height: 36px; border: 1px solid var(--ink-light); border-radius: 50%; margin: 0 auto;
  }
  .partner .mark-square {
    display: block; width: 38px; height: 26px; border: 1px solid var(--ink-light); margin: 0 auto 3px;
  }

  .capsule { position: absolute; left: 799px; top: 659px; width: 336px; height: 303px; }
  .capsule-top {
    position: absolute; left: 118px; top: 0; width: 99px; height: 99px; border-radius: 50%;
    background: var(--gold); border: 1px solid var(--gold-line);
  }
  .capsule-band {
    position: absolute; left: 3px; top: 99px; width: 330px; height: 18px;
    background: var(--gold); border: 1px solid var(--gold-line); border-bottom: none;
  }
  .capsule-rim {
    position: absolute; left: 0; top: 116px; width: 336px; height: 41px;
    background: var(--label-black); border-radius: 4px;
  }
  .capsule-body {
    position: absolute; left: 3px; top: 150px; width: 330px; height: 153px;
    background: var(--label-black);
  }
  .capsule-body .repeat {
    position: absolute; top: 94px; left: 0; right: 0; display: flex; justify-content: space-around;
  }
  .capsule-body .variety { font-size: 16px; }
</style>
</head>
<body>
<main class="canvas">

  <section class="front-label" aria-label="Etiqueta delantera">
    <div class="front-photo" role="img" aria-label="Fotografía de una cepa retorcida sobre una piedra de albariza con una uva verde en lo alto"></div>
    <h1 class="variety">Manzanilla</h1>
    <p class="council-note">Vino seleccionado por el Consejo Regulador<br>de la Denominación de Origen</p>
    <span class="measure volume">75 cl.</span>
    <span class="measure alcohol">15% vol.</span>
  </section>

  <section class="back-label" aria-label="Etiqueta trasera">
    <h2 class="variety">Manzanilla</h2>
    <p class="tagline">La niña bonita</p>
    <div class="origin-seal" role="img" aria-label="Sello de la Denominación de Origen"></div>
    <div class="partner-row">
      <div class="partner main">Campos Vivos Rurales</div>
      <div class="partner"><span class="mark-circle"></span>Junta de Verdalia</div>
      <div class="partner"><span class="mark-circle"></span></div>
      <div class="partner"><span class="mark-square"></span>Unión Albarena</div>
    </div>
  </section>

  <section class="capsule" aria-label="Cápsula">
    <div class="capsule-top"></div>
    <div class="capsule-band"></div>
    <div class="capsule-rim"></div>
    <div class="capsule-body">
      <div class="repeat">
        <span class="variety">Manzanilla</span>
        <span class="variety">Manzanilla</span>
        <span class="variety">Manzanilla</span>
      </div>
    </div>
  </section>

</main>
</body>
</html>
```